Lorna Tess Tresses Fancy Business Card’s

I want my business cards to be elite, original and very classy. I want the business cards to match the colors of my logo and to match the design posted. I would love the design of the picture I posted

I want the card all white .
The dripping on the top of the card I want it to match the pink color in my logo that’s also posted .
I need my logo on the business card !
I need my Instagram- @lorna.tess.tresses__
And my phone number - 582 907 3365

Target Market(s)

My target market is young woman age 23 to older woman to the age of 65
I want both older and younger women to love my design . I don’t want any cheap looking business cards

Industry/Entity Type

Hair And Beauty

Contact Information for Business Card

Add my logo
Add my Instagram- @lorna.tess.tresses__
My number - 582 907 3365
My website- www.lornatesstresses.example

Font styles to use
Serif
Script

Colors
ffffff
e667a6
e34298

Requirements
Must have
• The business cards must have my logo, my number , my website, and my Instagram!
Nice to have
• Nice to have glitter words that match my logo
• The business cards must look classy and mature
• I want them to be very unique!!
Should not have
• Should not have any colors that doesn’t match my logo ! This is very important! Please

```html
<!DOCTYPE html>
<html lang="en">
<head>
<meta charset="utf-8">
<title>Lorna Tess Tresses – Business Card</title>
<link rel="stylesheet" href="https://fonts.googleapis.com/css2?family=Lato:wght@400&display=swap">
<style>
  :root {
    --backdrop: #1f1f1f;
    --card-white: #ffffff;
    --brand-pink: #e34298;
    --brand-pink-soft: #e667a6;
    --brand-pink-pale: #f7c6df;
    --ink: #333333;
  }
  * { margin: 0; padding: 0; box-sizing: border-box; }
  html, body {
    width: 1200px; height: 900px; overflow: hidden;
    background: var(--backdrop);
    font-family: "Lato", sans-serif;
  }
  .stage { position: relative; width: 1200px; height: 900px; }

  .card {
    position: absolute; top: 200px;
    width: 310px; height: 502px;
    box-shadow: 3px 4px 6px rgba(0,0,0,0.55);
  }
  .card--front {
    left: 253px;
    background: var(--card-white);
    border-radius: 58px 0 58px 0;
  }
  .card--back {
    left: 627px;
    background: var(--brand-pink);
    border-radius: 0 58px 0 58px;
  }

  .brand-name {
    position: absolute; left: 0; right: 0;
    text-align: center;
    font-weight: 400;
    text-transform: uppercase;
    letter-spacing: 0.14em;
    line-height: 1.15;
  }
  .card--front .brand-name {
    top: 92px; color: var(--brand-pink);
    font-size: 38px;
  }
  .card--back .brand-name {
    top: 170px; color: var(--brand-pink-pale);
    font-size: 38px;
  }
  .brand-name .line { display: block; }
  .brand-name .line--small { font-size: 24px; letter-spacing: 0.4em; margin-top: 4px; }

  .contact-list {
    position: absolute; left: 32px; top: 366px;
    list-style: none;
    color: var(--ink);
    font-size: 17px;
  }
  .contact-item {
    display: flex; align-items: center; gap: 6px;
    height: 25px;
  }
  .contact-item--social { margin-top: 18px; }
  .contact-icon { width: 20px; height: 20px; flex: none; }
</style>
</head>
<body>
<main class="stage">
  <section class="card card--front" aria-label="Business card front">
    <h1 class="brand-name">
      <span class="line">Lorna Tess</span>
      <span class="line line--small">Tresses</span>
    </h1>
    <ul class="contact-list">
      <li class="contact-item">
        <svg class="contact-icon" viewBox="0 0 20 20" aria-hidden="true">
          <circle cx="10" cy="10" r="8.8" fill="none" stroke="var(--brand-pink)" stroke-width="1.4"/>
          <path d="M7 5.2l1.6 2.4-1 1.1c.6 1.4 1.6 2.4 3 3l1.1-1 2.4 1.6-.9 1.6c-3.6-.3-6.6-3.3-6.9-6.9z" fill="none" stroke="var(--brand-pink)" stroke-width="1.2" stroke-linejoin="round"/>
        </svg>
        <span>582 907 3365</span>
      </li>
      <li class="contact-item">
        <svg class="contact-icon" viewBox="0 0 20 20" aria-hidden="true">
          <g fill="none" stroke="var(--brand-pink)" stroke-width="1.4">
            <circle cx="10" cy="10" r="8.8"/>
            <ellipse cx="10" cy="10" rx="3.8" ry="8.8"/>
            <line x1="1.2" y1="10" x2="18.8" y2="10"/>
            <path d="M2.6 5.5h14.8M2.6 14.5h14.8"/>
          </g>
        </svg>
        <span>www.lornatesstresses.example</span>
      </li>
      <li class="contact-item contact-item--social">
        <svg class="contact-icon" viewBox="0 0 20 20" aria-hidden="true">
          <circle cx="10" cy="10" r="8.8" fill="none" stroke="var(--brand-pink)" stroke-width="1.4"/>
        </svg>
        <span>@lorna.tess.tresses</span>
      </li>
    </ul>
  </section>

  <section class="card card--back" aria-label="Business card back">
    <p class="brand-name">
      <span class="line">Lorna Tess</span>
      <span class="line line--small">Tresses</span>
    </p>
  </section>
</main>
</body>
</html>
```